Brivolo ( A new twist on task management )

We need modern, elegant, and clean (Quillon Design) on screens, buttons, and icons.

It is a (smart) task management application which helps the users to get notified and track task completion hassle free; Using notification profiles they create.

The interface of this application should be very simple and color schemes should be contemporary as long as they don’t make reading short text hard.

Following Quillon Design guidelines, the prefered font style is Roboto

Target Market(s)

Everyone from 13+

Industry/Entity Type

Software

Logo Text

Brivolo

Font styles to use
Other font styles liked:
• Roboto

```html
<!DOCTYPE html>
<html lang="en">
<head>
<meta charset="utf-8">
<title>Brivolo – Task Screens</title>
<link href="https://fonts.googleapis.com/css2?family=Roboto:wght@400;500;700&display=swap" rel="stylesheet">
<style>
  :root{
    --stage:#eef3ef;
    --surface:#eef0f2;
    --header:#a9b6bc;
    --header-text:#ffffff;
    --ink:#3a4a52;
    --ink-soft:#5d6c73;
    --divider:#c3cacd;
    --accent:#44575f;
    --accent-light:#b9c3c7;
    --field:#d3d9dc;
    --field-strong:#b6c1c6;
    --badge:#e0262b;
    --map:#e4e5e5;
    --map-road:#f6f6f6;
    --kbd:#7f9482;
    --key:#a4b5a6;
    --key-text:#ffffff;
    --avatar-a:#8a3a2e;
    --avatar-b:#d9a58c;
  }
  *{box-sizing:border-box;margin:0;padding:0}
  html,body{width:1200px;height:655px;overflow:hidden}
  body{background:var(--stage);font-family:"Roboto",sans-serif;color:var(--ink);position:relative}
  .screen{position:absolute;top:83px;width:237px;height:422px;background:var(--surface);overflow:hidden}
  .screen--tasks{left:46px}
  .screen--profile{left:336px}
  .screen--map{left:626px}
  .screen--new-task{left:917px}
  .abs{position:absolute}

  .status-bar{position:absolute;left:0;top:0;width:100%;height:12px;background:#fff;font-size:6.5px;display:flex;align-items:center;justify-content:space-between;padding:0 5px;color:#222}
  .status-bar .time{position:absolute;left:50%;transform:translateX(-50%)}
  .app-header{position:absolute;top:12px;left:0;width:100%;height:36px;background:var(--header);display:flex;align-items:center;color:var(--header-text)}
  .app-header .back{position:absolute;left:12px;top:11px}
  .app-header .title{position:absolute;left:0;right:0;text-align:center;font-weight:700;font-size:11px;letter-spacing:.3px;padding-right:28px}
  .app-header .search{position:absolute;right:50px;top:10px}
  .avatar{position:absolute;right:7px;top:5px;width:26px;height:26px;border-radius:50%;background:radial-gradient(circle at 55% 60%,var(--avatar-b),var(--avatar-a) 70%);border:1.5px solid #fff}
  .avatar-badge{position:absolute;right:4px;top:2px;width:10px;height:10px;border-radius:50%;background:var(--badge);color:#fff;font-size:6px;font-weight:700;display:flex;align-items:center;justify-content:center}

  .fab{position:absolute;width:28px;height:28px;border-radius:50%;background:var(--accent);display:flex;align-items:center;justify-content:center;box-shadow:0 1px 3px rgba(0,0,0,.25)}

  /* task list */
  .task-row{position:absolute;left:0;width:100%;border-bottom:1px dotted var(--divider)}
  .task-name{position:absolute;left:22px;font-size:10.5px;font-weight:700;color:var(--ink)}
  .task-lead{position:absolute;left:21px}
  .task-timer{position:absolute;left:38px;font-size:7.5px;font-weight:700}
  .icon{position:absolute;width:14px;height:14px;fill:none;stroke:var(--ink);stroke-width:1.4}

  /* profile */
  .pill-field{position:absolute;left:19px;top:109px;width:197px;height:24px;border-radius:12px;background:var(--field);font-size:7px;font-style:italic;color:var(--ink-soft);padding-left:12px;display:flex;align-items:center}
  .section-label{position:absolute;left:10px;top:162px;font-size:9.5px;font-weight:500;letter-spacing:.2px}
  .tabs{position:absolute;left:0;top:178px;width:100%;height:27px;display:flex}
  .tab{flex:1;display:flex;align-items:center;justify-content:center;font-size:9.5px;font-weight:700;color:#fff;background:var(--header)}
  .tab--active{background:var(--accent)}
  .setting{position:absolute;left:19px;font-size:9.5px;color:var(--ink)}
  .toggle{position:absolute;left:189px;top:236px;width:26px;height:13px;border-radius:7px;background:var(--accent)}
  .toggle::after{content:"";position:absolute;right:2px;top:2px;width:9px;height:9px;border-radius:50%;background:#fff}
  .slash{position:absolute;font-size:9.5px;color:var(--ink)}
  .action-bar{position:absolute;left:0;width:100%;height:33px;display:flex}
  .action{flex:1;display:flex;align-items:center;justify-content:center}
  .action--confirm{background:var(--accent-light)}
  .action--map-confirm{background:#ccd3d6}
  .action--cancel{background:var(--accent)}

  /* map */
  .map-area{position:absolute;left:0;top:46px;width:100%;height:338px;background:linear-gradient(160deg,var(--map),var(--map-road) 55%,var(--map))}
  .radius-bar{position:absolute;left:0;bottom:0;width:100%;height:38px;background:var(--header);display:flex;align-items:center;padding:0 10px;font-size:9px;color:var(--ink)}
  .radius-track{position:relative;flex:1;height:3px;background:#7d8c93;margin:0 8px 0 10px;border-radius:2px}
  .radius-thumb{position:absolute;left:72%;top:-3px;width:9px;height:9px;border-radius:50%;background:var(--accent)}
  .radius-value{font-size:7.5px;font-weight:700;color:#222}

  /* new task */
  .task-field{position:absolute;left:20px;top:119px;width:197px;height:28px;background:var(--field-strong);font-size:7.5px;font-style:italic;color:var(--ink-soft);padding-left:16px;display:flex;align-items:center}
  .field-divider{position:absolute;left:0;top:145px;width:100%;border-top:1px solid var(--divider)}
  .select-label{position:absolute;left:20px;top:161px;font-size:10px;color:var(--ink)}
  .profile-chip{position:absolute;top:152px;width:36px;height:27px;display:flex;align-items:center;justify-content:center}
  .profile-chip--location{left:136px;background:var(--accent)}
  .profile-chip--time{left:180px;background:#9fa9ad}
  .keyboard{position:absolute;left:0;top:271px;width:100%;height:151px;background:var(--kbd);padding:8px 2px 0}
  .key-row{display:flex;justify-content:center;gap:3.6px;margin-bottom:9px}
  .key{width:20px;height:27px;border-radius:4px;background:var(--key);color:var(--key-text);font-size:15px;display:flex;align-items:center;justify-content:center;padding-bottom:3px}
  .key--wide{width:28px;font-size:10px}
  .key--small{width:24px;font-size:9px}
  .key--space{width:90px;font-size:10px}
  .key--return{width:58px;font-size:10px}
</style>
</head>
<body>

<svg width="0" height="0" style="position:absolute">
  <defs>
    <symbol id="i-pin" viewBox="0 0 16 16"><path d="M9.5 2.5l4 4-2 .8-2.3 2.3.3 2.6-1 1-2.7-2.7L3 13.3M5.8 10.5L3.1 7.8l1-1 2.6.3L9 4.8z" stroke-linejoin="round"/></symbol>
    <symbol id="i-clock" viewBox="0 0 16 16"><circle cx="8" cy="8" r="6.3"/><path d="M8 4.5V8l2.4 1.6"/></symbol>
    <symbol id="i-place" viewBox="0 0 16 16"><path d="M8 14.8s-4.6-5-4.6-8.2a4.6 4.6 0 019.2 0C12.6 9.8 8 14.8 8 14.8z"/><circle cx="8" cy="6.5" r="1.7"/></symbol>
  </defs>
</svg>

<!-- Screen: active tasks -->
<section class="screen screen--tasks">
  <div class="status-bar"><span>●●●○○ mobile</span><span class="time">17:30 PM</span><span>100% ▭</span></div>
  <header class="app-header">
    <svg class="back" width="14" height="12" viewBox="0 0 14 12"><path d="M13 6H2M6.5 1.2L1.5 6l5 4.8" fill="none" stroke="#fff" stroke-width="1.6"/></svg>
    <span class="title">ACTIVE TASKS</span>
    <svg class="search" width="15" height="15" viewBox="0 0 15 15"><circle cx="6" cy="6" r="4.6" fill="none" stroke="#fff" stroke-width="1.7"/><path d="M9.4 9.4l4.3 4.3" stroke="#fff" stroke-width="1.9"/></svg>
    <div class="avatar" role="img" aria-label="User profile photo"></div>
    <span class="avatar-badge">5</span>
  </header>

  <div class="task-row" style="top:48px;height:59px">
    <svg class="task-lead" style="top:25px" width="7" height="9" viewBox="0 0 7 9"><path d="M1 .8l5 3.7-5 3.7z" fill="none" stroke="#3a4a52" stroke-width="1.1"/></svg>
    <span class="task-name" style="left:35px;top:22px">01 TASK</span>
    <svg class="icon" style="left:163px;top:23px"><use href="#i-pin"/></svg>
    <svg class="icon" style="left:188px;top:23px"><use href="#i-clock"/></svg>
    <svg class="icon" style="left:213px;top:22px"><use href="#i-place"/></svg>
  </div>
  <div class="task-row" style="top:107px;height:60px">
    <span class="abs" style="left:20px;top:20px;width:8px;height:8px;background:#3a4a52"></span>
    <span class="task-name" style="left:37px;top:17px">01 TASK</span>
    <span class="task-timer" style="left:38px;top:32px">00:15:30</span>
    <svg class="icon" style="left:163px;top:18px"><use href="#i-pin"/></svg>
    <svg class="icon" style="left:213px;top:17px"><use href="#i-place"/></svg>
  </div>
  <div class="task-row" style="top:167px;height:62px">
    <svg class="task-lead" style="top:24px" width="7" height="9" viewBox="0 0 7 9"><path d="M1 .8l5 3.7-5 3.7z" fill="none" stroke="#3a4a52" stroke-width="1.1"/></svg>
    <span class="task-name" style="left:35px;top:21px">01 TASK</span>
    <svg class="icon" style="left:163px;top:22px"><use href="#i-pin"/></svg>
    <svg class="icon" style="left:188px;top:22px"><use href="#i-clock"/></svg>
  </div>
  <div class="task-row" style="top:229px;height:63px">
    <svg class="task-lead" style="top:25px" width="7" height="9" viewBox="0 0 7 9"><path d="M1 .8l5 3.7-5 3.7z" fill="none" stroke="#3a4a52" stroke-width="1.1"/></svg>
    <span class="task-name" style="left:35px;top:22px">01 TASK</span>
    <svg class="icon" style="left:163px;top:24px"><use href="#i-pin"/></svg>
    <svg class="icon" style="left:213px;top:21px"><use href="#i-place"/></svg>
  </div>
  <div class="task-row" style="top:292px;height:58px">
    <svg class="task-lead" style="top:25px" width="7" height="9" viewBox="0 0 7 9"><path d="M1 .8l5 3.7-5 3.7z" fill="none" stroke="#3a4a52" stroke-width="1.1"/></svg>
    <span class="task-name" style="left:35px;top:22px">01 TASK</span>
    <svg class="icon" style="left:163px;top:24px"><use href="#i-pin"/></svg>
    <svg class="icon" style="left:213px;top:21px"><use href="#i-place"/></svg>
  </div>

  <div class="fab" style="left:201px;top:373px"><svg width="12" height="12" viewBox="0 0 12 12"><path d="M6 1v10M1 6h10" stroke="#fff" stroke-width="1.6"/></svg></div>
</section>

<!-- Screen: new profile -->
<section class="screen screen--profile">
  <div class="status-bar"><span>●●●○○ mobile</span><span class="time">17:30 PM</span><span>100% ▭</span></div>
  <header class="app-header">
    <svg class="back" width="14" height="12" viewBox="0 0 14 12"><path d="M13 6H2M6.5 1.2L1.5 6l5 4.8" fill="none" stroke="#fff" stroke-width="1.6"/></svg>
    <span class="title">NEW PROFILE</span>
    <svg class="search" width="15" height="15" viewBox="0 0 15 15"><circle cx="6" cy="6" r="4.6" fill="none" stroke="#fff" stroke-width="1.7"/><path d="M9.4 9.4l4.3 4.3" stroke="#fff" stroke-width="1.9"/></svg>
    <div class="avatar" role="img" aria-label="User profile photo"></div>
    <span class="avatar-badge">5</span>
  </header>
  <div class="fab" style="left:195px;top:63px"><svg width="12" height="12" viewBox="0 0 12 12"><path d="M6 1v10M1 6h10" stroke="#fff" stroke-width="1.6"/></svg></div>
  <div class="pill-field">ENTER PROFILE NAME</div>
  <div class="section-label">CHOOSE PROFILE TIGGERS</div>
  <div class="tabs"><div class="tab tab--active">LOCATION</div><div class="tab">TIME</div></div>
  <div class="setting" style="top:238px">TIME TIGGER</div>
  <div class="toggle"></div>
  <div class="setting" style="top:278px">SET START DATE</div>
  <div class="setting" style="top:318px">REPEAT EVERY</div>
  <div class="setting" style="top:358px">BETWEEN</div>
  <span class="slash" style="left:87px;top:358px">/</span><span class="slash" style="left:108px;top:358px">/</span>
  <div class="setting" style="left:155px;top:358px">AND</div>
  <span class="slash" style="left:188px;top:358px">/</span><span class="slash" style="left:209px;top:358px">/</span>
  <div class="action-bar" style="top:389px">
    <div class="action action--confirm"><svg width="24" height="18" viewBox="0 0 24 18"><path d="M2 9l7 7L22 2" fill="none" stroke="#44575f" stroke-width="2.4"/></svg></div>
    <div class="action action--cancel"><svg width="18" height="18" viewBox="0 0 18 18"><path d="M2 2l14 14M16 2L2 16" stroke="#c9d1d4" stroke-width="2.2"/></svg></div>
  </div>
</section>

<!-- Screen: location trigger map -->
<section class="screen screen--map">
  <div class="status-bar"><span>●●●○○ mobile</span><span class="time">17:30 PM</span><span>100% ▭</span></div>
  <div class="action-bar" style="top:12px;height:34px">
    <div class="action action--map-confirm"><svg width="24" height="18" viewBox="0 0 24 18"><path d="M2 9l7 7L22 2" fill="none" stroke="#44575f" stroke-width="2.4"/></svg></div>
    <div class="action action--cancel"><svg width="18" height="18" viewBox="0 0 18 18"><path d="M2 2l14 14M16 2L2 16" stroke="#c9d1d4" stroke-width="2.2"/></svg></div>
  </div>
  <div class="map-area" role="img" aria-label="Street map of the area around the trigger location"></div>
  <div class="radius-bar">
    <span>Tigger Radious</span>
    <div class="radius-track"><span class="radius-thumb"></span></div>
    <span class="radius-value">0.9 Km</span>
  </div>
</section>

<!-- Screen: new task -->
<section class="screen screen--new-task">
  <div class="status-bar"><span>●●●○○ mobile</span><span class="time">17:30 PM</span><span>100% ▭</span></div>
  <header class="app-header">
    <svg class="back" width="14" height="12" viewBox="0 0 14 12"><path d="M13 6H2M6.5 1.2L1.5 6l5 4.8" fill="none" stroke="#fff" stroke-width="1.6"/></svg>
    <span class="title">NEW TASK</span>
    <svg class="search" width="15" height="15" viewBox="0 0 15 15"><circle cx="6" cy="6" r="4.6" fill="none" stroke="#fff" stroke-width="1.7"/><path d="M9.4 9.4l4.3 4.3" stroke="#fff" stroke-width="1.9"/></svg>
    <div class="avatar" role="img" aria-label="User profile photo"></div>
    <span class="avatar-badge">5</span>
  </header>
  <div class="fab" style="left:196px;top:63px"><svg width="12" height="12" viewBox="0 0 12 12"><path d="M6 1v10M1 6h10" stroke="#fff" stroke-width="1.6"/></svg></div>
  <div class="task-field">Name of a Task</div>
  <div class="field-divider"></div>
  <div class="select-label">Select Profile</div>
  <div class="profile-chip profile-chip--location"><svg width="13" height="13" viewBox="0 0 16 16"><path d="M9.5 2.5l4 4-2 .8-2.3 2.3.3 2.6-1 1-2.7-2.7L3 13.3l2.8-2.8L3.1 7.8l1-1 2.6.3L9 4.8z" fill="#fff"/></svg></div>
  <div class="profile-chip profile-chip--time"><svg width="12" height="16" viewBox="0 0 12 16"><rect x="1.5" y="7" width="9" height="7.5" rx="1" fill="none" stroke="#fff" stroke-width="1.5"/><path d="M3.5 7V4.5a2.5 2.5 0 015 0" fill="none" stroke="#fff" stroke-width="1.5"/><circle cx="6" cy="10.7" r="1" fill="#fff"/></svg></div>

  <div class="keyboard">
    <div class="key-row"><span class="key">q</span><span class="key">w</span><span class="key">e</span><span class="key">r</span><span class="key">t</span><span class="key">y</span><span class="key">u</span><span class="key">i</span><span class="key">o</span><span class="key">p</span></div>
    <div class="key-row"><span class="key">a</span><span class="key">s</span><span class="key">d</span><span class="key">f</span><span class="key">g</span><span class="key">h</span><span class="key">j</span><span class="key">k</span><span class="key">l</span></div>
    <div class="key-row"><span class="key key--wide">⇧</span><span class="key">z</span><span class="key">x</span><span class="key">c</span><span class="key">v</span><span class="key">b</span><span class="key">n</span><span class="key">m</span><span class="key key--wide">⌫</span></div>
    <div class="key-row"><span class="key key--small">123</span><span class="key key--small">☺</span><span class="key key--small">🎤︎</span><span class="key key--space">space</span><span class="key key--return">return</span></div>
  </div>
</section>

</body>
</html>
```